(The Tide Lady) Cleaning swimming pool's & Spa's weekly for a monthly Rate

Name of company is (KRT Pool & Spa Cleaning) Lic.# 318604 __ KRT are initials for Kathy Rose Tellez, a female owner, nick name for her and company is (The Tide Lady) we would like to see Company and Nick name plus Lic. # on post card along with contact # 951-478-2051 call or Text and e-mail address(k_kwaterfresh@mailvale.com) No business Address posted being its our home address, also post an incentive to use our service as follows (50% off First Month of Maintenance, Very Reasonable Rate's !! ) incentive written in the middle of a picture of a Gorgeous swimming pool and to one side of picture is the silhouette profile of a woman with or without holding a pole with a cleaning net at end of pole, color of card maybe different shades of blue or just all blue. what we provide is a weekly cleaning maintenance service on in ground swimming pool's & Spa's, Thank you, Kathy

Target Market(s)

Home Owners with in ground swimming pools

Industry/Entity Type

It Company

Font styles to use
Serif
Decorative
Script

Requirements
Must have
• Silhouette outline profile design or picture of a woman next to a elegant swimming pool, colors of outline woman are to be contrast color like a pink or light grey against a blue background postcard
Nice to have
• nick name(The Tide Lady) and company name (KRT Pool & Spa Cleaning) on postcard, A small logo of a bar and shield stamp on one corner of card, KRT should read on bar, upper half of shield CLEAN should read and bottom half P00LS should read. uploaded files show bar and shield and possible picture of woman
Should not have
• None

```html
<!DOCTYPE html>
<html lang="en">
<head>
<meta charset="utf-8">
<title>KRT Pool &amp; Spa Cleaning – Postcard</title>
<link rel="stylesheet" href="https://fonts.googleapis.com/css2?family=Open+Sans:wght@400;600;700&display=swap">
<style>
  :root{
    --page:#e9ebee;
    --white:#ffffff;
    --sky:#6c92cc;
    --sky-deep:#3f66ad;
    --palm:#4d6a3c;
    --pool:#2f64ad;
    --pool-deep:#1c3d84;
    --panel:#2c5aa5;
    --panel-deep:#21468b;
    --mist:#eef0f3;
    --mist-shade:#dde1e7;
    --blush:#f4c9d6;
    --blush-soft:#e9b3c4;
    --shadow:rgba(0,0,0,.28);
  }
  *{box-sizing:border-box;margin:0;padding:0}
  html,body{width:1200px;height:856px;overflow:hidden}
  body{background:var(--page);font-family:"Open Sans",Arial,sans-serif;position:relative}

  .card{position:absolute;width:540px;height:370px;overflow:hidden;box-shadow:0 8px 22px var(--shadow)}
  .card--front{left:40px;top:60px}
  .card--back{left:620px;top:420px;background:var(--mist)}

  /* front */
  .front-photo{position:absolute;inset:0;
    background:
      radial-gradient(ellipse 60% 45% at 15% 55%,rgba(77,106,60,.85) 0%,rgba(77,106,60,0) 70%),
      radial-gradient(ellipse 70% 50% at 70% 80%,var(--pool) 0%,rgba(47,100,173,0) 75%),
      linear-gradient(180deg,var(--sky-deep) 0%,var(--sky) 25%,#7f8f8a 42%,var(--pool) 58%,var(--pool-deep) 100%);}
  .front-lines{position:absolute;inset:0}
  .front-title{position:absolute;left:30px;top:26px;color:var(--white);font-size:37px;font-weight:600;letter-spacing:.2px;text-shadow:0 2px 4px var(--shadow)}
  .front-offer{position:absolute;right:30px;top:82px;width:330px;text-align:right;color:var(--white);font-size:19px;line-height:1.2;text-shadow:0 1px 3px var(--shadow)}
  .front-silhouette{position:absolute;left:34px;top:140px;width:104px;height:176px;border-radius:52px 52px 8px 8px;
    background:linear-gradient(180deg,var(--blush) 0%,var(--blush-soft) 100%);opacity:.9}
  .front-phone{position:absolute;right:30px;top:232px;display:flex;align-items:center;gap:12px;color:var(--white);font-size:42px;font-weight:600;text-shadow:0 2px 4px var(--shadow)}
  .front-phone svg{width:38px;height:38px}
  .front-email{position:absolute;right:30px;top:296px;color:var(--white);font-size:13px;font-weight:600}
  .front-tag{position:absolute;left:30px;top:337px;color:var(--white);font-size:13px;font-weight:600;letter-spacing:.3px}

  /* back */
  .back-photo{position:absolute;left:215px;top:0;right:0;bottom:0;
    background:linear-gradient(170deg,var(--mist) 0%,var(--mist) 35%,var(--mist-shade) 60%,var(--mist) 100%)}
  .back-panel{position:absolute;left:0;top:0;bottom:0;width:215px;
    background:linear-gradient(180deg,var(--panel) 0%,var(--panel-deep) 100%);color:var(--white);padding:40px 24px 0 24px}
  .back-name{font-size:27px;line-height:1.2;font-weight:400;text-shadow:0 2px 3px var(--shadow)}
  .back-name strong{font-weight:700}
  .back-tag{margin-top:12px;font-size:12px;line-height:1.35;font-weight:600}
  .back-offer{margin-top:22px;font-size:13px;line-height:1.3}
  .back-call{margin-top:16px;font-size:21px;font-weight:600;line-height:1.15;text-shadow:0 2px 3px var(--shadow)}
  .back-email{margin-top:20px;font-size:9.5px;font-weight:600;white-space:nowrap}
</style>
</head>
<body>

<article class="card card--front">
  <div class="front-photo" role="img" aria-label="Photo of a resort swimming pool lined with palm trees and villas under a blue sky"></div>
  <svg class="front-lines" width="540" height="370" viewBox="0 0 540 370" aria-hidden="true">
    <line x1="0" y1="325" x2="540" y2="325" stroke="#ffffff" stroke-opacity=".45" stroke-width="1"/>
    <line x1="250" y1="0" x2="250" y2="40" stroke="#ffffff" stroke-opacity=".3" stroke-width="1"/>
  </svg>
  <h1 class="front-title">KRT Pool &amp; Spa Cleaning</h1>
  <p class="front-offer">50% off First Month of Maintenance, Very Reasonable Rate's !!</p>
  <div class="front-silhouette" role="img" aria-label="Light pink silhouette profile of a woman holding a pool pole with a cleaning net"></div>
  <p class="front-phone">
    <svg viewBox="0 0 24 24" aria-hidden="true"><path fill="#ffffff" d="M6.6 10.8a15.1 15.1 0 0 0 6.6 6.6l2.2-2.2a1 1 0 0 1 1-.25 11.4 11.4 0 0 0 3.6.57 1 1 0 0 1 1 1V20a1 1 0 0 1-1 1A17 17 0 0 1 3 4a1 1 0 0 1 1-1h3.5a1 1 0 0 1 1 1c0 1.25.2 2.46.57 3.6a1 1 0 0 1-.25 1z"/></svg>
    951-478-2051
  </p>
  <p class="front-email">e-mail: (k_kwaterfresh@mailvale.com)</p>
  <p class="front-tag">The Tide Lady &nbsp;·&nbsp; Lic.# 318604</p>
</article>

<article class="card card--back">
  <div class="back-photo" role="img" aria-label="Faded photo of a swimming pool with palm trees"></div>
  <div class="back-panel">
    <h2 class="back-name"><strong>KRT</strong> Pool &amp;<br>Spa Cleaning</h2>
    <p class="back-tag">The Tide Lady<br>Lic.# 318604</p>
    <p class="back-offer">50% off First Month of Maintenance, Very Reasonable Rate's !!</p>
    <p class="back-call">CALL US<br>951-478-2051</p>
    <p class="back-email">e-mail: (k_kwaterfresh@mailvale.com)</p>
  </div>
</article>

</body>
</html>
```